Tea box package for Herbal Teas

We would like a design for a package of our tea products. We want the consumer to understand that our products are natural just by looking at the package. We prefer minimalistic designs.
The package we want would be a square (or slightly rectangular) box. The box would be generic enough for us to use it for different teas. Essentially what we want is all the main information and designs to be the same for each tea product we have. We would like to be able to change the main color and the name of the tea then to customize to the tea in the package. Please see the attached images for examples.
We really like the package in tea_packaging_example_4 picture. We would like our packaging to be something very similar but with all the labels printed on the package.
We already have our logo so I am attaching that as well (image named 'velk ansary logo copy'). That would go on the front of the box.
We also attach a tile created using our logo (see image called 'tile'). We would like this to go to the sides similarly to tea_packaging_example_4.
On the back of the pouch, we want to have directions on how to make the tea but we want this section to be editable. For now just 3-4 lines of sample text is fine along with instructions on how to make a tea, see picture 'back of tea box'.
We would like for the box color to be as in example picture
tea_packaging_example_4. The color of the writing should be the same as the logo color. The font style should be something that would look nice next to the logo font, we are not sure what that font should be. The only thing colored would be the name of the tea and the ribbon as seen in tea_packaging_example_4, which we would like to change if we need to, to other variations.
Thanks a lot. For any questions, please contact me.

```html
<!DOCTYPE html>
<html lang="en">
<head>
<meta charset="utf-8">
<title>Velk Ansary – Reverie Tea Box</title>
<link href="https://fonts.googleapis.com/css2?family=Cormorant+Garamond:wght@500&family=Montserrat:wght@700;800&display=swap" rel="stylesheet">
<style>
  :root {
    --canvas-bg: #e6e6e6;
    --box-white: #f6f7f9;
    --box-edge: #d6d7da;
    --band-olive: #b7b786;
    --ribbon-yellow: #dcd862;
    --ink: #2e2e2e;
    --pattern-olive: #c9c9a2;
    --pattern-light: #eef0ea;
  }
  * { box-sizing: border-box; margin: 0; padding: 0; }
  html, body { width: 1200px; height: 685px; overflow: hidden; }
  body { background: var(--canvas-bg); position: relative; font-family: "Montserrat", sans-serif; color: var(--ink); }

  .panel { position: absolute; background: var(--box-white); overflow: hidden; }
  .panel-top { left: 620px; top: 45px; width: 380px; height: 200px; }
  .panel-side { left: 240px; top: 245px; width: 380px; height: 400px; border-top: 1px solid var(--box-edge); border-right: 1px solid var(--box-edge); }
  .panel-front { left: 620px; top: 245px; width: 380px; height: 400px; border-top: 1px solid var(--box-edge); }

  .tile-pattern {
    position: absolute; inset: 14px 0 0 14px;
    background: linear-gradient(135deg, var(--pattern-olive) 0%, var(--pattern-light) 50%, var(--pattern-olive) 100%);
  }

  .band { position: absolute; left: 105px; width: 185px; background: var(--band-olive); }
  .panel-top .band { top: 0; height: 100%; display: flex; align-items: center; justify-content: center; }
  .panel-front .band { top: 0; height: 270px; }

  .brand { display: flex; flex-direction: column; align-items: center; gap: 10px; }
  .brand-dot { width: 40px; height: 40px; border-radius: 50%; background: var(--ink); }
  .brand-name { font-family: "Cormorant Garamond", serif; font-weight: 500; font-size: 25px; letter-spacing: 0.5px; text-transform: uppercase; color: var(--ink); white-space: nowrap; }
  .panel-top .brand-name { font-size: 21px; }
  .panel-top .brand-dot { width: 32px; height: 32px; }
  .panel-front .brand { position: absolute; top: 70px; left: 0; width: 100%; }

  .category { position: absolute; top: 18px; left: 0; width: 100%; text-align: center; font-size: 8px; font-weight: 800; letter-spacing: 3px; text-transform: uppercase; white-space: nowrap; }

  .ribbon { position: absolute; left: 105px; top: 270px; width: 185px; height: 72px; background: var(--ribbon-yellow); text-align: center; padding-top: 9px; }
  .tea-name { font-size: 19px; font-weight: 800; letter-spacing: 2px; text-transform: uppercase; line-height: 1; }
  .tea-notes { font-size: 7px; font-weight: 800; letter-spacing: 2px; text-transform: uppercase; line-height: 1.3; margin-top: 3px; }
  .count { position: absolute; left: 105px; top: 350px; width: 185px; text-align: center; font-size: 15px; font-weight: 700; line-height: 1; }
  .contents { position: absolute; left: 85px; top: 373px; width: 225px; text-align: center; font-size: 7px; font-weight: 800; letter-spacing: 3px; text-transform: uppercase; white-space: nowrap; }
</style>
</head>
<body>
  <section class="panel panel-top">
    <div class="band">
      <div class="brand">
        <span class="brand-dot"></span>
        <span class="brand-name">Velk Ansary</span>
      </div>
    </div>
  </section>

  <section class="panel panel-side">
    <div class="tile-pattern" role="img" aria-label="Repeating olive and white tile pattern built from the brand emblem"></div>
  </section>

  <section class="panel panel-front">
    <div class="band">
      <p class="category">Organic Herbal Tea</p>
      <div class="brand">
        <span class="brand-dot"></span>
        <span class="brand-name">Velk Ansary</span>
      </div>
    </div>
    <div class="ribbon">
      <h1 class="tea-name">Reverie</h1>
      <p class="tea-notes">White Peony<br>Jasmine</p>
    </div>
    <p class="count">12</p>
    <p class="contents">Handcrafted Tea Balls</p>
  </section>
</body>
</html>
```